Q827 PowerPoint Presentation

As you can see the design of this PowerPoint isn't cohesive. There are a lot of images and words that give it a very jumbled and busy appeal. We want to turn this into a sharp, cohesive and visually appealing presentation without taking away too much of the information. Feel free to use the images to create your own artwork for the PowerPoint.

Please don't hesitate to contact me with any questions.

```html
<!DOCTYPE html>
<html lang="en">
<head>
<meta charset="utf-8">
<title>Q827 Presentation Overview</title>
<link rel="stylesheet" href="https://fonts.googleapis.com/css2?family=Open+Sans:wght@300;400;600;700&display=swap">
<style>
:root{
  --stage:#d6d7d9;
  --paper:#ffffff;
  --teal:#5ba4bd;
  --teal-light:#8cc3d4;
  --orange:#f47a2b;
  --navy:#2f4a63;
  --slate:#3d5872;
  --ink:#3b4654;
  --muted:#8a96a3;
  --rule:#c9ced4;
  --label:#d2d4d7;
}
*{box-sizing:border-box;margin:0;padding:0}
html,body{width:1200px;height:700px;overflow:hidden}
body{background:var(--stage);font-family:"Open Sans",Arial,sans-serif;color:var(--ink);position:relative}
.slide{position:absolute;background:var(--paper);box-shadow:0 1px 4px rgba(0,0,0,.25);overflow:hidden}
.slide-title{position:absolute;left:0;right:0;text-align:center;font-weight:400;letter-spacing:.3px;color:var(--ink)}
.slide-title .accent{color:var(--teal)}
.footer{position:absolute;left:0;right:0;bottom:0;height:16px;background:linear-gradient(90deg,#8aa6bd,var(--slate) 45%,var(--navy));color:#fff;font-size:5.5px;display:flex;align-items:center;justify-content:center}
.footer .icons{position:absolute;left:8px;top:50%;transform:translateY(-50%);display:flex;gap:4px}
.footer .icons span{width:6px;height:6px;background:#fff;opacity:.85;display:block}
.pointer{position:absolute;height:1px;background:var(--rule)}
.pointer::after{content:"";position:absolute;right:-2px;top:-2px;width:5px;height:5px;border-radius:50%;background:var(--teal)}
.tiny{font-size:4.5px;line-height:1.45;color:var(--muted)}
.tiny .hi{color:var(--orange)}
.tiny .tl{color:var(--teal)}

/* Ideas to reality */
.ideas{left:16px;top:26px;width:373px;height:208px}
.ideas .slide-title{top:9px;font-size:10px}
.ideas .sub{position:absolute;left:88px;top:48px;font-size:5px;color:var(--ink)}
.ideas .sub .hi{color:var(--orange)}
.chevrons{position:absolute;left:62px;top:72px}
.chev-notes{position:absolute;top:120px;display:flex;gap:8px;left:70px}
.chev-notes p{width:70px}

/* Process */
.process{left:16px;top:245px;width:373px;height:213px}
.process .slide-title{top:8px;font-size:9px}
.process h4{position:absolute;left:48px;font-size:5.5px;font-weight:600;color:var(--ink)}
.process h4 .tl{color:var(--teal)}
.process ul{position:absolute;left:56px;list-style:none;width:110px}
.process .cycle{position:absolute;left:190px;top:34px;width:160px;height:156px;border-radius:50%;background:radial-gradient(circle,#3d5872 0 18%,#6fa9c0 40%,#d7e8ef 72%,rgba(255,255,255,0) 74%)}

/* Main */
.main{left:402px;top:15px;width:778px;height:443px;background:linear-gradient(180deg,#f6f7f8,#e9ebee)}
.main .head{position:absolute;left:0;right:0;top:0;height:62px;background:var(--paper);border-bottom:1px solid var(--rule)}
.main .slide-title{top:15px;font-size:20px;font-weight:300;color:var(--slate)}
.main .slide-title b{font-weight:400;color:var(--navy)}
.main .tagline{position:absolute;left:84px;top:106px;font-size:15px;font-weight:400;color:#222}
.main .tagline .hi{color:var(--orange)}
.devices{position:absolute;left:112px;top:140px;width:300px;height:260px;border-radius:8px;background:linear-gradient(160deg,#c9ced4,#f4f5f6 45%,#b8bec6)}
.features{position:absolute;left:482px;top:97px;list-style:none}
.features li{position:absolute;left:0;display:flex;height:27px}
.features .num{width:32px;background:var(--teal);color:#fff;font-size:13px;display:flex;align-items:center;justify-content:center;font-weight:300}
.features .label{width:200px;background:var(--label);font-size:8px;display:flex;align-items:center;padding-left:8px;color:var(--ink);letter-spacing:.2px}
.features .sub{left:30px}
.features .sub .num{width:24px;font-size:10px}
.features .sub .label{background:#fafafa;width:168px}
.main .footer{height:31px;font-size:9px}
.main .footer .icons{left:18px;gap:10px}
.main .footer .icons span{width:11px;height:11px}

/* Dashboard */
.dash{left:16px;top:472px;width:374px;height:210px;background:linear-gradient(135deg,#dfe7ee,#6d8aa3 55%,var(--navy))}
.dash .slide-title{top:5px;font-size:9.5px}
.shot{position:absolute;border:1px solid #fff;background:linear-gradient(135deg,#e8ecf0,#9fb2c3)}
.dash .note{position:absolute;color:#fff;font-size:4.8px;line-height:1.5;width:88px}

/* System benefits */
.system{left:405px;top:472px;width:374px;height:210px}
.system .slide-title{top:7px;font-size:8.5px}
.system .your{position:absolute;left:43px;top:46px;font-size:5.5px;font-weight:600}
.system .your span{color:var(--teal)}
.system ul{position:absolute;left:44px;top:68px;list-style:none;font-size:4.6px;line-height:1.6;color:var(--ink)}
.system .pyramid{position:absolute;left:200px;top:40px}
.callout{position:absolute;display:flex;align-items:center;gap:4px;background:var(--orange);color:#fff;font-size:3.8px;line-height:1.3;padding:3px 4px}
.callout i{width:8px;height:8px;border-radius:50%;border:1px solid #fff;flex:none}

/* Realised benefits */
.realised{left:799px;top:472px;width:378px;height:210px}
.realised .slide-title{top:9px;font-size:8.5px}
.realised .panel{position:absolute;left:0;top:30px;width:186px;height:164px;background:linear-gradient(135deg,#b9cad8,#4d6a84 55%,var(--navy))}
.realised .monitor{position:absolute;left:28px;top:14px;width:130px;height:100px;border-radius:3px;background:linear-gradient(160deg,#d5dbe1,#f4f5f6 50%,#aab3bd)}
.realised ul{position:absolute;left:196px;top:50px;width:170px;list-style:none;font-size:4.3px;line-height:1.45;color:var(--ink)}
.realised li.note{color:var(--teal);text-align:center}
</style>
</head>
<body>

<section class="slide ideas">
  <h2 class="slide-title">IDEAS <span class="accent" style="font-size:7px">TO</span> <span class="accent">REALITY</span></h2>
  <div class="pointer" style="left:0;top:51px;width:84px"></div>
  <p class="sub">A <span class="hi">suite based</span> environment for architecture <span class="hi">decision analytics</span></p>
  <svg class="chevrons" width="250" height="46" viewBox="0 0 250 46" aria-hidden="true">
    <polygon points="0,0 78,0 94,23 78,46 0,46 16,23" fill="#8cc3d4"/>
    <polygon points="80,0 158,0 174,23 158,46 80,46 96,23" fill="#2f4a63"/>
    <polygon points="160,0 234,0 250,23 234,46 160,46 176,23" fill="#f47a2b"/>
    <g fill="#fff" font-family="Open Sans, sans-serif" font-size="4.5" text-anchor="middle">
      <rect x="44" y="9" width="8" height="9" rx="1"/><text x="48" y="34">THE CHALLENGE</text>
      <rect x="122" y="9" width="9" height="9" transform="rotate(45 126.5 13.5)"/><text x="127" y="34">THE NEED</text>
      <polygon points="205,7 211,18 199,18"/><text x="205" y="34">THE RESULT</text>
    </g>
  </svg>
  <div class="chev-notes tiny">
    <p>Identifying and integrating an organisation's sources of record for budget, systems and reference.</p>
    <p>A <span class="hi">portal</span> solution enabling the rapid capture, organisation and analysis of data from <span class="hi">multiple</span> sources.</p>
    <p>A <span class="hi">collaborative</span> architecture decision support tool that drives cost savings and mission <span class="hi">success</span>.</p>
  </div>
  <footer class="footer"><div class="icons"><span></span><span></span><span></span></div>Ideas to Reality 2014 ©</footer>
</section>

<section class="slide process">
  <h2 class="slide-title"><span>THE</span> <span class="accent">PROCESS</span></h2>
  <div class="pointer" style="left:0;top:48px;width:44px"></div>
  <h4 style="top:44px"><span class="tl">Q827</span> PROVIDES DATA INTEGRATION:</h4>
  <ul class="tiny" style="top:54px">
    <li>• <span class="hi">Integrates</span> data feeds from internal and external sources</li>
    <li>• <span class="hi">Updates</span> can be made at any point of the cycle</li>
    <li>• Changes to any data component are tested for impact</li>
    <li>• Updates take effect <span class="hi">immediately</span></li>
    <li>• Provides the most <span class="hi">current</span> data available</li>
    <li>• Makes data analysis more accessible</li>
  </ul>
  <div class="pointer" style="left:0;top:124px;width:44px"></div>
  <h4 style="top:120px"><span class="tl">Q827</span> DESIGN ALLOWS ORGANISATIONS TO:</h4>
  <ul class="tiny" style="top:130px">
    <li>• Justify programs</li>
    <li>• Show decision <span class="hi">impacts</span></li>
    <li>• Display <span class="hi">traceability</span> of programs to strategies</li>
    <li>• At individual level</li>
    <li>• Provide <span class="hi">annual</span> budget data</li>
    <li>• Include all possible systems in database</li>
    <li>• Associate current utilisation requirements and current effort</li>
  </ul>
  <div class="cycle" role="img" aria-label="Star-shaped decision cycle diagram linking capability requirements, gap analysis, program initiation, investment decisions and products"></div>
  <footer class="footer"><div class="icons"><span></span><span></span><span></span></div>Ideas to Reality 2014 ©</footer>
</section>

<section class="slide main">
  <div class="head"><h1 class="slide-title"><b>Q827</b> DISCOVERY PLATFORM</h1></div>
  <div class="pointer" style="left:0;top:113px;width:78px"></div>
  <p class="tagline">MULTI-DEVICE, <span class="hi">MOBILE</span> and <span class="hi">DESKTOP</span> Ready!</p>
  <div class="devices" role="img" aria-label="Desktop monitor and smartphone showing the analytics dashboard with a map, pie chart and bar charts"></div>
  <ul class="features">
    <li style="top:0"><span class="num">01</span><span class="label">MODULAR TOOL ARCHITECHTURE</span></li>
    <li style="top:34px"><span class="num">02</span><span class="label">EXTENSIBLE WIDGED FRAMEWORK</span></li>
    <li style="top:68px"><span class="num">03</span><span class="label">REAL TIME DATA EVENTS</span></li>
    <li style="top:102px"><span class="num">04</span><span class="label">SEMANTIC &amp; CONCEPT</span></li>
    <li class="sub" style="top:131px"><span class="num">4b</span><span class="label">Searching</span></li>
    <li style="top:161px"><span class="num">05</span><span class="label">ENTITY &amp; FACET SEARCHING</span></li>
    <li style="top:194px"><span class="num">06</span><span class="label">USER DEFINABLE DATA</span></li>
    <li class="sub" style="top:224px"><span class="num">6b</span><span class="label">Other</span></li>
  </ul>
  <footer class="footer"><div class="icons"><span></span><span></span><span></span></div>Ideas to Reality 2014 ©</footer>
</section>

<section class="slide dash">
  <h2 class="slide-title">KDA <span class="accent">DASHBOARD INIATIVE</span></h2>
  <div class="shot" style="left:6px;top:30px;width:92px;height:40px" role="img" aria-label="Dashboard home screen"></div>
  <div class="shot" style="left:6px;top:84px;width:100px;height:48px" role="img" aria-label="Dashboard data tables"></div>
  <div class="shot" style="left:110px;top:88px;width:100px;height:44px" role="img" aria-label="Dashboard gauges"></div>
  <div class="shot" style="left:212px;top:88px;width:100px;height:44px" role="img" aria-label="Dashboard pie chart view"></div>
  <div class="shot" style="left:6px;top:140px;width:96px;height:52px" role="img" aria-label="Dashboard detail screen"></div>
  <p class="note" style="left:112px;top:32px">• Provides a 1 stop interactive display to address the health of the agency<br>• Facilitates decision making with drill down to greater levels of detail at a click</p>
  <p class="note" style="left:212px;top:32px">• Uses business rules supported by an Enterprise Scoring System to provide near real time updates of agency health</p>
  <p class="note" style="left:112px;top:150px">• Fosters automated system to system interaction to gain copy authoritative data providing the most current data available</p>
  <p class="note" style="left:212px;top:150px">• Supports KDA executives with plans to provide dashboards down to the supervisor level</p>
  <footer class="footer"><div class="icons"><span></span><span></span><span></span></div>Ideas to Reality 2014 ©</footer>
</section>

<section class="slide system">
  <h2 class="slide-title">SYSTEM <span class="accent">BENEFITS</span></h2>
  <div class="pointer" style="left:0;top:48px;width:38px"></div>
  <p class="your">YOUR <span>TITLE</span></p>
  <ul>
    <li>• Activate Document → Entity Analysis Platform</li>
    <li>• Convert Unstructured Multi-lingual Text into Insights</li>
    <li>• Simple, Intuitive Search Analytics</li>
    <li>• From Data Mining to Entity Mining</li>
    <li>• Automatic Link Analysis &amp; <span style="color:var(--orange)">Inferencing</span></li>
  </ul>
  <p class="tiny" style="position:absolute;left:44px;top:112px;width:140px">Each input item is resolved to a unique entity and then linked across sources so that analysts see a single, reliable view of every record drawn from many places.</p>
  <div class="callout" style="left:42px;top:146px;width:142px"><i></i>Short note on how this benefit helps teams decide faster and save effort.</div>
  <svg class="pyramid" width="120" height="112" viewBox="0 0 120 112" aria-hidden="true">
    <polygon points="60,0 72,20 48,20" fill="#f47a2b"/>
    <polygon points="48,22 72,22 84,42 36,42" fill="#8cc3d4"/>
    <polygon points="36,44 84,44 96,64 24,64" fill="#6fa9c0"/>
    <polygon points="24,66 96,66 108,86 12,86" fill="#4f86a3"/>
    <polygon points="12,88 108,88 120,110 0,110" fill="#2f4a63"/>
    <g font-family="Open Sans, sans-serif" font-size="4" fill="#fff" text-anchor="middle">
      <text x="60" y="15">Insight</text><text x="60" y="34">Intelligence</text>
      <text x="60" y="56">Knowledge</text><text x="60" y="78">Information</text>
      <text x="60" y="101">Data</text>
    </g>
  </svg>
  <footer class="footer"><div class="icons"><span></span><span></span><span></span></div>Ideas to Reality 2014 ©</footer>
</section>

<section class="slide realised">
  <h2 class="slide-title">REALISED <span class="accent">BENEFITS</span></h2>
  <div class="panel">
    <div class="monitor" role="img" aria-label="Monitor showing the analytics dashboard with map and charts"></div>
    <div class="callout" style="left:26px;top:128px;width:150px"><i></i>Short note on the measured savings seen after the platform went live.</div>
  </div>
  <ul>
    <li>• Identified the need to create a common taxonomy</li>
    <li class="note">Allowing for simplified data association/visualisation/display</li>
    <li>• Significantly reduced data call response time for budget and congressional inquiries</li>
    <li class="note">Required data compiled rapidly and accurately in response to data call at all levels of the enterprise</li>
    <li>• Assisted in plans alignment to the most current guidance and requirements</li>
    <li class="note">Annual guidance updates occasionally result in plan alignment or requirements</li>
    <li>• Provided integrated analysis of live systems, requirements and products data which allowed in-depth analysis of system contributions to functional capabilities</li>
    <li>• Aligned budget data with production data allowing for cost analysis per product and system justification</li>
    <li>• Savings in personnel research and compilation hours</li>
  </ul>
  <footer class="footer"><div class="icons"><span></span><span></span><span></span></div>Ideas to Reality 2014 ©</footer>
</section>

</body>
</html>
```